Schlichtes Website-Design für Mineralwasser
Zielgruppe
TILMO ist eine neue hochwertige Mineralwassermarke, die online bestellt werden kann. Der Stil von TILMO ist geradlinig, futuristisch, skandinavisch, minimalistisch und eher kühl. Der Markenname TILMO ist von dem lateinischen „aer“ abgeleitet und steht für das Wort „Luft“. Das Attribut „luftig-leicht“ soll daher auch im Design der Webseite wiederzufinden sein.
Die Zielgruppe für TILMO ist breit gefächert und umfasst nicht nur Privatpersonen (Studenten, Berufstätige, Familien, Singlehaushalte, ältere Personen u. a. m.) sondern auch Gewerbe, die sich Mineralwasser ins Büro liefern lassen wollen.
Aufgabenstellung
1. Es soll ein Design für die Webseite von TILMO erstellt werden, die denselben Aufbau wie die Webseite moos-perle.de hat, aber an die Wassermarke TILMO angepasst wird. Hier ist bereits die Richtung des Website-Designs mit verschiedenen Elementen, die den Screen ausfüllen, schön dargestellt.
2. Bisher ist von der Marke TILMO nur das Flaschenetikett vorhanden. Das Design der Webseite soll sich daran orientieren.
3. Das Design soll so gestaltet sein, dass in der Entwicklung eine responsive Webseite gut möglich ist. Das Design an sich soll nur für die Desktopansicht gestaltet werden.
4. Gerne kann an kleine Animationen gedacht werden, die bei der Entwicklung der Seite mit eingebaut werden können, um die Seite aufzulockern.

```html
<!DOCTYPE html>
<html lang="de">
<head>
<meta charset="utf-8">
<title>TILMO Mineralwasser</title>
<link rel="stylesheet" href="https://fonts.googleapis.com/css2?family=Marcellus&family=Open+Sans:wght@400;600&display=swap">
<style>
:root{
  --navy:#26268a;
  --laut:#3b45c9;
  --leise:#3c9fe6;
  --still:#e5463d;
  --text:#8a8a8f;
  --page:#e6e6e8;
  --paper:#ffffff;
  --photo-top:#f3f5f8;
  --photo-bottom:#e6eaf0;
  --dot:#b9b9c2;
}
*{margin:0;padding:0;box-sizing:border-box}
html,body{width:1200px;height:2700px;overflow:hidden}
body{background:radial-gradient(ellipse at center,#f7f7f8 0%,var(--page) 100%);font-family:"Open Sans",sans-serif;position:relative}
h1,h2{font-weight:400}
.sheet{position:absolute;left:82px;top:0;width:1036px;height:2700px;background:var(--paper);overflow:hidden}
.wave-area{position:absolute;left:0;width:1036px}
.wave-top{top:0;height:130px;background:linear-gradient(180deg,rgba(196,224,248,.55) 0%,rgba(226,240,252,.35) 55%,rgba(255,255,255,0) 100%)}
.wave-bottom{top:2610px;height:90px;background:linear-gradient(0deg,rgba(222,226,234,.6) 0%,rgba(255,255,255,0) 100%)}
.brand{position:absolute;left:0;width:1036px;text-align:center;top:14px;font-family:"Marcellus",serif;color:var(--navy)}
.brand-name{font-size:46px;letter-spacing:4px;line-height:1}
.brand-sub{font-size:13px;letter-spacing:1.5px;color:#7f7fb8;margin-top:2px}
.photo{position:absolute;border-radius:4px}
.hero-photo{left:358px;top:82px;width:330px;height:348px;background:linear-gradient(180deg,var(--photo-top),var(--photo-bottom))}
.laut-photo{left:439px;top:566px;width:418px;height:485px;background:linear-gradient(90deg,var(--photo-top) 0%,var(--photo-bottom) 55%,#dfe4fa 100%)}
.leise-photo{left:180px;top:1100px;width:398px;height:488px;background:linear-gradient(90deg,#dceefb 0%,var(--photo-bottom) 45%,var(--photo-top) 100%)}
.still-photo{left:439px;top:1649px;width:418px;height:489px;background:linear-gradient(90deg,var(--photo-top) 0%,var(--photo-bottom) 55%,#fbe1e1 100%)}
.slogan{position:absolute;left:0;width:1036px;top:442px;text-align:center;font-family:"Marcellus",serif;font-size:22px;color:var(--navy)}
.intro{position:absolute;left:278px;width:480px;top:470px;text-align:center;font-size:7.5px;line-height:12px;color:var(--text)}
.mouse{position:absolute;width:14px;height:24px;border:1.4px solid #9a9aa6;border-radius:7px}
.mouse::after{content:"";position:absolute;left:5px;top:5px;width:1.4px;height:6px;background:#9a9aa6}
.product-title{position:absolute;font-family:"Marcellus",serif;font-size:26px;color:var(--navy);white-space:nowrap;line-height:1}
.product-text{position:absolute;font-size:8px;line-height:18px;color:var(--text);width:188px}
.align-right{text-align:right}
.order-btn{position:absolute;width:137px;height:18px;border:1.6px solid;border-radius:3px;font-family:"Marcellus",serif;font-size:8.5px;letter-spacing:2.6px;text-align:center;line-height:15px}
.watermark{position:absolute;left:0;width:1036px;text-align:center;font-family:"Marcellus",serif;color:#f6f6f8;line-height:1}
.watermark-name{top:2285px;font-size:165px;letter-spacing:18px}
.watermark-sub{top:2470px;font-size:46px;letter-spacing:8px}
.minerals-title{position:absolute;left:0;width:1036px;top:2297px;text-align:center;font-family:"Marcellus",serif;font-size:22px;color:var(--navy)}
.mineral-table{position:absolute;top:2390px;width:190px;font-size:8.5px;color:var(--navy);border-collapse:collapse}
.mineral-table caption{text-align:left;font-family:"Marcellus",serif;font-size:12px;padding-bottom:7px;white-space:nowrap}
.mineral-table th{text-align:left;font-weight:400;height:24.5px;white-space:nowrap}
.mineral-table td{text-align:left;color:var(--text);width:40px}
.table-divider{position:absolute;left:517px;top:2392px;width:1px;height:110px;background:#d6d6de}
.footer-note{position:absolute;left:218px;top:2678px;font-size:5.5px;color:#8a8a96}
.footer-link{position:absolute;left:769px;top:2676px;font-family:"Marcellus",serif;font-size:8px;color:var(--navy)}
.section-nav{position:absolute;left:1098px;width:8px}
.section-nav span{display:block;width:4px;height:4px;border-radius:50%;background:var(--dot);margin:0 auto 4px}
.section-nav span.on{width:8px;height:8px;background:var(--navy);box-shadow:inset 0 0 0 1.5px #fff,0 0 0 1px var(--navy)}
</style>
</head>
<body>
<main class="sheet">
  <div class="wave-area wave-top" role="img" aria-label="Feine hellblaue Wellenlinien als Kopfdekoration"></div>

  <div class="brand">
    <div class="brand-name">TILMO</div>
    <div class="brand-sub">MINERALWASSER</div>
  </div>

  <div class="photo hero-photo" role="img" aria-label="Drei TILMO Glasflaschen: Still, Laut und Leise"></div>
  <h1 class="slogan">SLOGAN&nbsp; HEADER TEXT WILL GO HERE</h1>
  <p class="intro">Purer Geschmack trifft klares Design. Die schlichte Eleganz reduziert TILMO auf den Inhalt: reines Wasser. Frisch von der Quelle spiegelt TILMO Wasser eine bewusste Lebensweise wider. Laut, leise, still... TILMO Wasser überzeugt mit seinen drei Charakteren</p>
  <div class="mouse" style="left:511px;top:505px"></div>

  <div class="photo laut-photo" role="img" aria-label="TILMO Laut in PET- und Glasflasche mit blauen Luftblasen"></div>
  <h2 class="product-title" style="right:629px;top:736px">TILMO <span style="color:var(--laut)">LAUT</span></h2>
  <p class="product-text align-right" style="left:219px;top:775px">TILMO Laut ist herrlich sprudelnd sowie reich an Mineralstoffen. Das natürliche Mineralwasser ist erfrischend und rein im Geschmack. TILMO Laut ist die richtige Wahl für alle, die Mineralwasser am liebsten prickelnd mögen.</p>
  <div class="order-btn" style="left:270px;top:884px;color:var(--navy);border-color:var(--navy)">JETZ BESTELLEN</div>

  <div class="photo leise-photo" role="img" aria-label="TILMO Leise in Glas- und PET-Flasche mit hellblauen Luftblasen"></div>
  <h2 class="product-title" style="left:628px;top:1275px">TILMO <span style="color:var(--leise)">LEISE</span></h2>
  <p class="product-text" style="left:628px;top:1315px;width:190px">Für alle, die es gerne ein wenig ruhiger haben, bietet TILMO Leise eine belebend sanfte Erfrischung. Durch die milde Kohlensäure ist das Wasser natürlich zurückhaltend und fein perlend im Geschmack.</p>
  <div class="order-btn" style="left:627px;top:1424px;color:var(--leise);border-color:var(--leise)">JETZ BESTELLEN</div>

  <div class="photo still-photo" role="img" aria-label="TILMO Still in PET- und Glasflasche mit rotem Wasserspritzer"></div>
  <h2 class="product-title" style="right:629px;top:1828px">TILMO <span style="color:var(--still)">STILL</span></h2>
  <p class="product-text align-right" style="left:219px;top:1867px">TILMO Still belebt auf sanfte und natürliche Art. Wer ein Wasser ohne Kohlensäure genießen will und den natürlichen Geschmack von Wasser mag, greift zu TILMO Still.</p>
  <div class="order-btn" style="left:270px;top:1976px;color:var(--still);border-color:var(--still)">JETZ BESTELLEN</div>

  <div class="watermark watermark-name" aria-hidden="true">TILMO</div>
  <div class="watermark watermark-sub" aria-hidden="true">MINERALWASSER</div>
  <h2 class="minerals-title">NATÜRLICHES MINERALWASSER</h2>

  <table class="mineral-table" style="left:303px">
    <caption>KATIONEN IN MG/L</caption>
    <tr><th>NATRIUM:</th><td>19,0</td></tr>
    <tr><th>CALCIUM:</th><td>110,2</td></tr>
    <tr><th>MAGNESIUM:</th><td>5,9</td></tr>
    <tr><th>KALIUM:</th><td>1,28</td></tr>
  </table>
  <div class="table-divider"></div>
  <table class="mineral-table" style="left:552px">
    <caption>ANIONEN IN MG/L</caption>
    <tr><th>CHLORID:</th><td>42,0</td></tr>
    <tr><th>FLUORID:</th><td>0,08</td></tr>
    <tr><th>SULFAT:</th><td>73,0</td></tr>
    <tr><th>HYDROGENCARBONAT:</th><td>240,0</td></tr>
  </table>

  <div class="wave-area wave-bottom" role="img" aria-label="Feine graue Wellenlinien als Fußdekoration"></div>
  <div class="mouse" style="left:511px;top:2646px"></div>
  <p class="footer-note">Quellhain Getränke GmbH &nbsp;|&nbsp; 24103 Kiel &nbsp;|&nbsp; All Right Reserved</p>
  <a class="footer-link">IMPRESSUM</a>
</main>

<nav class="section-nav" style="top:243px"><span class="on"></span><span></span><span></span><span></span><span></span></nav>
<nav class="section-nav" style="top:785px"><span></span><span class="on"></span><span></span><span></span><span></span></nav>
<nav class="section-nav" style="top:1327px"><span></span><span></span><span class="on"></span><span></span><span></span></nav>
<nav class="section-nav" style="top:1867px"><span></span><span></span><span></span><span class="on"></span><span></span></nav>
<nav class="section-nav" style="top:2360px"><span></span><span></span><span></span><span></span><span class="on"></span></nav>
</body>
</html>
```